Company Playbill Advertisement Design

I own a production company that provides audio,lighting,video, and other production services to events and conventions. I am sponsoring a event and they are giving me a full page ad in the playbill. It needs to be Full Page (Full Bleed) Trim Area: 5.5” x 8.5” Image Area: 5” x 8”. I would like the design to include photos, information about my company, and my logo in a professional presentation to lure potential clients to contact us. We are a production company so it needs to be something that catches your eye but professional.

Target Market(s)

Companies looking for production services. Our customer is mainly a professional person looking for services. We are not a DJ company so our market is a bit smaller.

Industry/Entity Type

Events

Requirements
Must have
• Company phone number is 555-407-2918, website is www.brivenstagecrew.example. Company Logo, photos of events.
• Accepted Ad Formats: .jpg, .pdf., .eps. Full Color Minimum 300 dpi All Fonts Outlined. It needs to be Full Page (Full Bleed) Trim Area: 5.5” x 8.5” Image Area: 5” x 8”.
Nice to have
• Creative design that catches someone eye. We are a creative company so we want our ad to reflect that.

```html
<!DOCTYPE html>
<html lang="en">
<head>
<meta charset="utf-8">
<title>Briven Stage Crew – Playbill Advertisement</title>
<link rel="stylesheet" href="https://fonts.googleapis.com/css2?family=Open+Sans:wght@400;600;700;800&family=Rubik:wght@900&display=swap">
<style>
  :root {
    --ink: #111111;
    --white: #ffffff;
    --band: #151412;
    --accent-red: #e01e1e;
    --teal-glow: #7fe3cf;
    --teal-deep: #1d5a52;
    --night: #0c1512;
    --violet: #3b2a5c;
    --forest: #1f3b2a;
    --paper: #ffffff;
  }
  * { margin: 0; padding: 0; box-sizing: border-box; }
  html, body { width: 777px; height: 1200px; overflow: hidden; background: var(--paper); }
  body { font-family: "Open Sans", Arial, sans-serif; color: var(--white); }
  .ad { position: relative; width: 777px; height: 1200px; overflow: hidden; background: var(--paper); }

  .hero-photo {
    position: absolute; left: 0; top: 0; width: 777px; height: 580px;
    background:
      radial-gradient(ellipse 260px 200px at 440px 410px, rgba(160,255,230,0.75), rgba(60,150,130,0.3) 60%, transparent 80%),
      radial-gradient(ellipse 420px 300px at 480px 250px, rgba(120,220,200,0.45), transparent 75%),
      linear-gradient(180deg, #1b2a26 0%, #2e5e55 45%, #1a3a33 75%, #070a09 100%);
  }
  .crowd-fade {
    position: absolute; left: 0; top: 520px; width: 777px; height: 60px;
    background: linear-gradient(180deg, transparent, rgba(5,8,7,0.9));
  }

  .headline {
    position: absolute; left: 54px; top: 58px;
    font-family: "Rubik", Arial, sans-serif; font-weight: 900;
    font-size: 30px; line-height: 35px; letter-spacing: 0.5px; text-transform: uppercase;
  }
  .headline span { display: inline-block; background: rgba(20,20,20,0.72); padding: 0 8px 0 8px; }
  .headline .period { background: none; color: var(--accent-red); }

  .brand-mark {
    position: absolute; display: flex; align-items: center; gap: 8px;
    font-family: "Open Sans", Arial, sans-serif; font-weight: 800; letter-spacing: 0.5px;
  }
  .brand-mark .dot { width: 14px; height: 14px; background: var(--accent-red); }
  .brand-mark--hero { right: 56px; top: 66px; font-size: 17px; color: var(--white); }
  .brand-mark--footer { left: 54px; top: 1118px; font-size: 20px; color: var(--ink); }

  .about-band {
    position: absolute; left: 0; top: 580px; width: 777px; height: 80px;
    background: var(--band); display: flex; align-items: center;
  }
  .about-label {
    position: absolute; left: 50px; top: 40px; transform: translate(-50%,-50%) rotate(-90deg);
    font-family: "Rubik", Arial, sans-serif; font-weight: 900; font-size: 18px; line-height: 15px; text-align: left;
  }
  .about-label small { display: block; font-family: "Open Sans", Arial, sans-serif; font-weight: 800; font-size: 8px; line-height: 10px; letter-spacing: 0.5px; }
  .about-text { margin-left: 114px; width: 620px; font-size: 14.4px; line-height: 18px; }

  .services {
    position: absolute; left: 0; top: 660px; width: 777px; height: 432px;
    background:
      linear-gradient(180deg, rgba(25,20,30,0.55), rgba(15,25,20,0.7) 40%, rgba(40,30,80,0.85) 100%),
      linear-gradient(90deg, var(--violet), var(--forest) 45%, #4a2f3a 70%, var(--violet));
  }
  .services-title {
    position: absolute; left: 54px; top: 20px;
    font-family: "Rubik", Arial, sans-serif; font-weight: 900; font-size: 42px; line-height: 50px;
    display: flex; align-items: center;
  }
  .services-title .we-do { display: inline-flex; flex-direction: column; font-size: 15px; line-height: 14px; margin: 0 6px 0 12px; }
  .service { position: absolute; width: 320px; }
  .service--left { left: 54px; text-align: left; }
  .service--right { right: 54px; text-align: right; }
  .service h3 { font-weight: 600; font-size: 22px; line-height: 26px; text-transform: uppercase; letter-spacing: 0.2px; }
  .service p { font-size: 12.8px; line-height: 14.6px; }

  .footer-contact {
    position: absolute; right: 54px; top: 1112px; text-align: right; color: var(--ink);
    font-weight: 700; font-size: 20px; line-height: 24px;
  }
</style>
</head>
<body>
<main class="ad">
  <div class="hero-photo" role="img" aria-label="Concert photo: festival stage with teal beams of light through haze, truss towers, an aerial performer and a cheering crowd"></div>
  <div class="crowd-fade"></div>

  <h1 class="headline">
    <span>The best sales,</span><br>
    <span>production, and</span><br>
    <span>rental company</span><br>
    <span>you need in</span><br>
    <span>Central Florida.</span><br>
    <span class="period">Period.</span>
  </h1>

  <div class="brand-mark brand-mark--hero"><span class="dot"></span>Briven Stage Crew</div>

  <section class="about-band">
    <div class="about-label">WHO<small>WE ARE?</small></div>
    <p class="about-text">Briven Stage Crew or BSC is your source for events, sales, production services, and entertainment in the Central Florida area. We can meet your needs in a hurry. We excel in the live event category with over 14 years experience in shows and festivals.</p>
  </section>

  <section class="services" role="img" aria-label="Background photo: festival crowd with confetti under colourful stage lights">
    <h2 class="services-title">WHAT<span class="we-do"><span>WE</span><span>DO</span></span>?</h2>

    <div class="service service--left" style="top:98px"><h3>Audio Services</h3><p>BSC has some of the best<br>audio gear so you can be heard</p></div>
    <div class="service service--left" style="top:160px"><h3>Lighting Services</h3><p>We have the latest in automated<br>lighting fixtures</p></div>
    <div class="service service--left" style="top:222px"><h3>Event Video</h3><p>BSC has a full line of LED walls<br>and projectors to fit any event and budget</p></div>
    <div class="service service--left" style="top:283px"><h3>Effects</h3><p>Fog, Haze, Snow, Cryo C02, Confetti,<br>Pyro, Low Lying Fog</p></div>
    <div class="service service--left" style="top:345px"><h3>Rigging</h3><p>We can elevate your event by providing<br>trussing, motors, or towers to hang<br>anything that needs to be put up</p></div>

    <div class="service service--right" style="top:98px"><h3>Mobile / Deck Staging</h3><p>We can provide any size mobile or<br>deck stage for your needs</p></div>
    <div class="service service--right" style="top:160px"><h3>Event Management</h3><p>We can take your event ideas<br>and make them a success</p></div>
    <div class="service service--right" style="top:222px"><h3>Sales and Install</h3><p>We provide the best gear for any situation<br>and will train you on how to use it</p></div>
    <div class="service service--right" style="top:283px"><h3>Equipment Rentals</h3><p>BSC is a great source for rental gear.<br>Audio, Lighting, Video, LED Wall, Staging</p></div>
    <div class="service service--right" style="top:345px"><h3>Equipment Rentals</h3><p>We partner with the award-winning team<br>at Lumenpath Visual Studios on all video<br>and film production services</p></div>
  </section>

  <div class="brand-mark brand-mark--footer"><span class="dot"></span>Briven Stage Crew</div>
  <div class="footer-contact">555-407-2918<br>www.brivenstagecrew.example</div>
</main>
</body>
</html>
```